Website Redesign - Money is Guaranteed!

I would like a site similar to this: http://www.givewheelsforheroes.example

old site: http://www.autosforpatriots.example

Create a professional website; a car donation site seeking leads to return calls.

Please see http://www.givewheelsforheroes.example for the concept I am after.

The webpage should have a professional feel. The pages to include are 'Home', 'About us' and 'Get Started'

Industry/Entity Type

It Professional

Coding

Coded - Design and coding required

Number of Pages Required

1 page

```html
<!DOCTYPE html>
<html lang="en">
<head>
<meta charset="utf-8">
<title>Autos for Patriots – Donate Your Car</title>
<link href="https://fonts.googleapis.com/css2?family=Raleway:wght@300;400;600;700&family=Open+Sans:wght@400;600;700&display=swap" rel="stylesheet">
<style>
:root{
  --red:#b3121a;
  --red-dark:#7e0b10;
  --ink:#3a3a3a;
  --muted:#8a8a8a;
  --line:#e2e2e2;
  --bg:#ffffff;
  --soft:#f5f5f5;
  --white:#ffffff;
}
*{box-sizing:border-box;margin:0;padding:0}
html,body{width:1200px;height:2184px;overflow:hidden;background:var(--bg)}
body{position:relative;font-family:"Open Sans",Arial,sans-serif;color:var(--ink)}
h1,h2,h3{font-family:"Raleway",Arial,sans-serif;font-weight:300}

/* header */
.site-header{position:absolute;top:0;left:0;width:1200px;height:60px;background:var(--white);display:flex;align-items:center;padding:0 120px 0 112px;border-bottom:1px solid var(--line)}
.brand{display:flex;align-items:center;gap:10px;font-family:"Open Sans",sans-serif;font-weight:700;font-size:17px;color:var(--red);letter-spacing:.5px}
.brand-mark{width:18px;height:18px;background:var(--red)}
.main-nav{margin-left:auto;display:flex;align-items:center;gap:40px;font-size:12px;font-weight:600;letter-spacing:1px}
.main-nav a{color:var(--ink);text-decoration:none}
.main-nav .nav-cta{background:var(--red);color:var(--white);padding:11px 20px}

/* hero */
.hero{position:absolute;top:60px;left:0;width:1200px;height:500px}
.hero-photo{position:absolute;inset:0;background:linear-gradient(100deg,#6e6e6e 0%,#9b9b9b 40%,#c9c9c9 65%,#8a1a1e 85%,#5a0d10 100%)}
.hero-copy{position:absolute;left:112px;top:200px;color:var(--white)}
.hero-copy h1{font-size:40px;font-weight:400;line-height:1.1}
.hero-copy p{font-family:"Raleway",sans-serif;font-size:30px;font-weight:300;margin-top:4px}
.btn{display:inline-block;background:var(--red);color:var(--white);font-size:12px;font-weight:700;letter-spacing:1px;padding:13px 22px;text-decoration:none}
.hero-copy .btn{margin-top:26px}
.lead-form{position:absolute;left:740px;top:40px;width:340px;height:440px;background:rgba(255,255,255,.96);box-shadow:0 4px 16px rgba(0,0,0,.25)}
.lead-form-head{background:var(--red);color:var(--white);text-align:center;padding:18px 0 14px}
.lead-form-head .call{font-size:12px;font-weight:600;letter-spacing:2px}
.lead-form-head .phone{font-size:30px;font-weight:700;letter-spacing:1px;line-height:1.2}
.lead-form-head .note{font-size:9px;letter-spacing:1px}
.fields{padding:16px 20px 0;display:grid;grid-template-columns:1fr 1fr;gap:10px}
.field{height:32px;border:1px solid #d6d6d6;background:var(--white);font-size:11px;color:#999;padding:8px 10px}
.field.full{grid-column:span 2}
.field.select{position:relative}
.field.select::after{content:"";position:absolute;right:10px;top:13px;border:4px solid transparent;border-top-color:#999}
.lead-form .submit{display:block;margin:14px 20px 0;text-align:center;background:var(--red);color:var(--white);font-size:12px;font-weight:700;padding:12px 0}

/* how it works */
.how{position:absolute;top:560px;left:0;width:1200px;height:420px;background:var(--white)}
.section-title{font-size:30px;color:var(--ink);position:absolute;left:112px}
.how .section-title{top:66px}
.steps{position:absolute;top:128px;left:112px;display:flex;gap:64px}
.step{width:276px;height:236px;border:1px solid var(--line);padding:26px 24px;position:relative}
.step svg{width:44px;height:44px}
.step-num{position:absolute;right:24px;top:24px;width:40px;height:40px;background:var(--red);color:var(--white);font-size:20px;font-weight:600;display:flex;align-items:center;justify-content:center}
.step h3{font-size:21px;font-weight:400;color:var(--ink);letter-spacing:1px;margin-top:14px}
.step p{font-size:11px;color:var(--muted);line-height:1.6;margin-top:12px}
.divider{position:absolute;top:980px;left:0;width:1200px;height:1px;background:var(--line)}

/* why donate */
.why{position:absolute;top:981px;left:0;width:1200px;height:719px}
.why .section-title{top:86px}
.benefits{position:absolute;top:160px;left:112px;display:grid;grid-template-columns:repeat(3,300px);column-gap:20px;row-gap:40px}
.benefit{display:flex;gap:14px;min-height:82px}
.benefit svg{flex:none;width:32px;height:32px}
.benefit h4{font-size:12px;font-weight:700;color:var(--ink)}
.benefit p{font-size:10.5px;color:var(--muted);line-height:1.55;margin-top:6px}

/* call to action */
.cta{position:absolute;top:1700px;left:0;width:1200px;height:380px}
.cta-photo{position:absolute;inset:0;background:linear-gradient(110deg,#8e1016 0%,#b8232a 45%,#d7545a 70%,#9b1419 100%)}
.cta-body{position:absolute;left:112px;top:50px;color:var(--white)}
.cta-body h2{font-size:32px;font-weight:300}
.checklist{list-style:none;margin-top:20px}
.checklist li{display:flex;align-items:center;gap:10px;font-size:12px;font-weight:600;margin-bottom:10px}
.checklist svg{width:14px;height:14px}
.cta-body .btn{margin-top:12px;background:var(--white);color:var(--red)}

/* footer */
.site-footer{position:absolute;top:2080px;left:0;width:1200px;height:104px;background:var(--white);display:flex;align-items:center;padding:0 112px}
.badges{display:flex;gap:16px;align-items:center}
.badge-round{width:46px;height:46px;border-radius:50%;background:#2c4a7a}
.badge-rect{width:72px;height:30px;background:#c8c8c8}
.copyright{position:absolute;left:0;right:0;text-align:center;font-size:10px;color:var(--muted)}
</style>
</head>
<body>

<header class="site-header">
  <div class="brand"><span class="brand-mark"></span>Autos for Patriots</div>
  <nav class="main-nav">
    <a href="#">HOME</a>
    <a href="#">ABOUT US</a>
    <a href="#" class="nav-cta">GET STARTED</a>
  </nav>
</header>

<section class="hero">
  <div class="hero-photo" role="img" aria-label="Close-up photo of a red car parked on a city street"></div>
  <div class="hero-copy">
    <h1>Donate Your Car To A Vet</h1>
    <p>Make A Difference</p>
    <a href="#" class="btn">DONATE NOW!</a>
  </div>
  <form class="lead-form">
    <div class="lead-form-head">
      <div class="call">CALL US TODAY</div>
      <div class="phone">1-800-555-0142</div>
      <div class="note">LICENSED / INSURED - 7 DAYS A WEEK</div>
    </div>
    <div class="fields">
      <div class="field">First Name</div>
      <div class="field">Last Name</div>
      <div class="field full">Email Address</div>
      <div class="field full">Phone</div>
      <div class="field select">Vehicle Year</div>
      <div class="field select">Vehicle Make</div>
      <div class="field">Model</div>
      <div class="field">Zip Code</div>
    </div>
    <div class="submit">Click to Donate Your Car</div>
  </form>
</section>

<section class="how">
  <h2 class="section-title">How It Works</h2>
  <div class="steps">
    <div class="step">
      <svg viewBox="0 0 44 44" fill="none" stroke="#b3121a" stroke-width="2"><path d="M10 6h8l3 9-5 3a22 22 0 0 0 10 10l3-5 9 3v8c0 2-2 4-4 4C19 38 6 25 6 10c0-2 2-4 4-4z"/></svg>
      <div class="step-num">1</div>
      <h3>CALL US</h3>
      <p>Give us a call and our friendly team will take down your vehicle details and answer any question.</p>
    </div>
    <div class="step">
      <svg viewBox="0 0 44 44" fill="none" stroke="#b3121a" stroke-width="2"><rect x="3" y="12" width="22" height="18"/><path d="M25 18h8l7 7v5H25z"/><circle cx="11" cy="33" r="4"/><circle cx="33" cy="33" r="4"/></svg>
      <div class="step-num">2</div>
      <h3>WE TOW IT</h3>
      <p>We arrange free pickup at a time that suits you, whether your car runs or not, anywhere nearby.</p>
    </div>
    <div class="step">
      <svg viewBox="0 0 44 44" fill="none" stroke="#b3121a" stroke-width="2"><path d="M10 4h18l8 8v28H10z"/><path d="M28 4v8h8"/><path d="M16 20h14M16 26h14M16 32h9"/></svg>
      <div class="step-num">3</div>
      <h3>TAX RIGHT OFF</h3>
      <p>Receive your receipt by mail and claim a tax deduction for the fair value of your donated car.</p>
    </div>
  </div>
</section>

<div class="divider"></div>

<section class="why">
  <h2 class="section-title">Why Donate Your Car to Us?</h2>
  <div class="benefits">
    <div class="benefit">
      <svg viewBox="0 0 32 32" fill="none" stroke="#555" stroke-width="1.6"><circle cx="16" cy="16" r="14"/><path d="M9 16l5 5 9-10"/></svg>
      <div><h4>IRS policy Approved</h4><p>Your gift is fully recognized under current IRS charitable giving rules.</p></div>
    </div>
    <div class="benefit">
      <svg viewBox="0 0 32 32" fill="none" stroke="#555" stroke-width="1.6"><rect x="2" y="9" width="16" height="13"/><path d="M18 13h6l5 5v4H18z"/><circle cx="8" cy="24" r="3"/><circle cx="24" cy="24" r="3"/></svg>
      <div><h4>Free Local Towing to You</h4><p>We can pick up your donation, running or not, from any location in our service area.</p></div>
    </div>
    <div class="benefit">
      <svg viewBox="0 0 32 32" fill="none" stroke="#555" stroke-width="1.6"><path d="M4 20l3-8h18l3 8v5H4z"/><circle cx="10" cy="25" r="2.5"/><circle cx="22" cy="25" r="2.5"/></svg>
      <div><h4>All Cars Accepted</h4><p>We accept cars, trucks, vans and more in any condition or registration status.</p></div>
    </div>
    <div class="benefit">
      <svg viewBox="0 0 32 32" fill="none" stroke="#555" stroke-width="1.6"><circle cx="16" cy="16" r="14"/><path d="M20 11h-6a3 3 0 0 0 0 6h4a3 3 0 0 1 0 6h-6M16 8v16"/></svg>
      <div><h4>Donate Tax Deduction</h4><p>You may qualify to deduct the fair market value of your vehicle on your taxes.</p></div>
    </div>
    <div class="benefit">
      <svg viewBox="0 0 32 32" fill="none" stroke="#555" stroke-width="1.6"><path d="M7 3h13l6 6v20H7z"/><path d="M11 14h11M11 19h11M11 24h7"/></svg>
      <div><h4>No Paperwork Hassles</h4><p>We take care of every form and title transfer. No hassles.</p></div>
    </div>
    <div class="benefit">
      <svg viewBox="0 0 32 32" fill="none" stroke="#555" stroke-width="1.6"><path d="M16 28S4 20 4 11a6 6 0 0 1 12-2 6 6 0 0 1 12 2c0 9-12 17-12 17z"/></svg>
      <div><h4>Car donations help Fundraising</h4><p>Your donated vehicle helps local programs supporting veterans and their families.</p></div>
    </div>
    <div class="benefit">
      <svg viewBox="0 0 32 32" fill="none" stroke="#555" stroke-width="1.6"><circle cx="16" cy="16" r="14"/><path d="M16 8v8l5 4"/></svg>
      <div><h4>Schedule a free Pickup</h4><p>Complete the form or call our representative and we will arrange a convenient pickup for you.</p></div>
    </div>
  </div>
</section>

<section class="cta">
  <div class="cta-photo" role="img" aria-label="Photo of a hand holding out car keys, tinted red"></div>
  <div class="cta-body">
    <h2>Donate Your Car Today!</h2>
    <ul class="checklist">
      <li><svg viewBox="0 0 14 14" fill="none" stroke="#fff" stroke-width="2"><path d="M2 7l3 3 7-7"/></svg>You have no costs</li>
      <li><svg viewBox="0 0 14 14" fill="none" stroke="#fff" stroke-width="2"><path d="M2 7l3 3 7-7"/></svg>Free towing, running or not</li>
      <li><svg viewBox="0 0 14 14" fill="none" stroke="#fff" stroke-width="2"><path d="M2 7l3 3 7-7"/></svg>We issue you an IRS tax receipt</li>
      <li><svg viewBox="0 0 14 14" fill="none" stroke="#fff" stroke-width="2"><path d="M2 7l3 3 7-7"/></svg>We take care of all paperwork</li>
      <li><svg viewBox="0 0 14 14" fill="none" stroke="#fff" stroke-width="2"><path d="M2 7l3 3 7-7"/></svg>And we take care of DMV &amp; Smog issues</li>
    </ul>
    <a href="#" class="btn">DONATE NOW!</a>
  </div>
</section>

<footer class="site-footer">
  <div class="badges">
    <span class="badge-round"></span>
    <span class="badge-rect"></span>
  </div>
  <p class="copyright">Copyright © 2016 Autos for Patriots. All Rights Reserved.</p>
</footer>

</body>
</html>
```